Author/ Speaker Business Card design

I need a business card designed that will go with the branding that is already on my book and website. I like clean and straightforward, but I am not opposed to something more 'innovative'.

Target Market(s)

Colleges and Universities, educational institutions

Industry/Entity Type

Education

Contact Information for Business Card

Standard size. It should be able to be printed on good quality white or ivory paper.

Font styles to use
Sans Serif

Colors
0355a3

Requirements
Must have
• There's a blue on my website. It should have some blue. My logo is at the top. It should have the logo incorporated somewhere on it. My name, Author | Speaker | Teacher | Trainer, my phone number (+31 64-207 5184), my email address (milo@thebrightlearner.example), Social media icons (twitter, Instagram, LinkedIn) with the addresses (twitter @writermilohart, Instagram - thebrightlearner, LinkedIn - thebrightlearner) By they way, the website is www.thebrightlearner.example. There is a photo of the book on the website. Also, my full name is Milo Hart
Nice to have
• Try to use the font that is on the website and book. Also, if you could get that blue, that would be great.
Should not have
• My photo

```html
<!DOCTYPE html>
<html lang="en">
<head>
<meta charset="utf-8">
<title>The Bright Learner – Business Card</title>
<link rel="stylesheet" href="https://fonts.googleapis.com/css2?family=Lato:wght@400;700;900&display=swap">
<style>
  :root {
    --brand-blue: #0355a3;
    --ink: #1c1c1c;
    --paper: #ffffff;
    --backdrop: #3b3b3b;
  }
  * { box-sizing: border-box; margin: 0; padding: 0; }
  html, body {
    width: 1200px; height: 1200px; overflow: hidden;
    background: var(--backdrop);
    font-family: 'Lato', sans-serif;
  }
  .card {
    position: absolute; left: 150px;
    width: 900px; height: 514px;
  }
  .card-back { top: 60px; background: var(--brand-blue); }
  .card-front { top: 626px; background: var(--paper); color: var(--ink); }

  .back-wordmark {
    position: absolute; left: 470px; top: 150px;
    color: var(--paper); font-weight: 900;
    font-size: 84px; line-height: 0.95; letter-spacing: -1px;
  }

  .front-wordmark {
    position: absolute; left: 0; right: 0; top: 80px;
    text-align: center; color: var(--brand-blue);
    font-weight: 900; font-size: 70px; letter-spacing: -1px;
  }

  .identity {
    position: absolute; right: 470px; top: 262px; text-align: right;
  }
  .identity-name {
    color: var(--brand-blue); font-weight: 900; font-size: 38px;
    letter-spacing: -0.5px; line-height: 1.1;
  }
  .identity-roles { font-size: 23px; margin-top: 6px; white-space: nowrap; }
  .identity-roles .sep { color: var(--brand-blue); padding: 0 3px; }

  .divider {
    position: absolute; left: 450px; top: 262px;
    width: 2px; height: 96px; background: var(--brand-blue);
  }

  .contacts {
    position: absolute; left: 478px; top: 258px; list-style: none;
    font-size: 21px; line-height: 34px;
  }
  .contacts li { display: flex; align-items: center; gap: 14px; white-space: nowrap; }
  .contacts svg { width: 20px; height: 20px; fill: var(--brand-blue); flex: none; }

  .socials {
    position: absolute; left: 0; right: 0; top: 420px;
    display: flex; justify-content: center; gap: 34px; list-style: none;
    font-size: 23px;
  }
  .socials li { display: flex; align-items: center; gap: 10px; }
  .socials .marker {
    width: 14px; height: 14px; background: var(--brand-blue); border-radius: 3px;
  }
</style>
</head>
<body>

<section class="card card-back">
  <div class="back-wordmark">The<br>Bright<br>Learner</div>
</section>

<section class="card card-front">
  <div class="front-wordmark">The Bright Learner</div>

  <div class="identity">
    <div class="identity-name">MILO HART</div>
    <div class="identity-roles">Author<span class="sep">|</span>Speaker<span class="sep">|</span>Teacher<span class="sep">|</span>Trainer</div>
  </div>

  <div class="divider"></div>

  <ul class="contacts">
    <li>
      <svg viewBox="0 0 24 24" aria-hidden="true"><path d="M6.6 10.8a15 15 0 0 0 6.6 6.6l2.2-2.2a1 1 0 0 1 1-.25 11.4 11.4 0 0 0 3.6.57 1 1 0 0 1 1 1V20a1 1 0 0 1-1 1A17 17 0 0 1 3 4a1 1 0 0 1 1-1h3.5a1 1 0 0 1 1 1c0 1.25.2 2.45.57 3.6a1 1 0 0 1-.25 1z"/></svg>
      +31 64-207 5184
    </li>
    <li>
      <svg viewBox="0 0 24 24" aria-hidden="true"><path d="M2 5h20v14H2zm2 2v.4l8 5.2 8-5.2V7zm0 2.8V17h16V9.8l-8 5.2z"/></svg>
      milo@thebrightlearner.example
    </li>
    <li>
      <svg viewBox="0 0 24 24" aria-hidden="true"><path d="M12 2a10 10 0 1 0 0 20 10 10 0 0 0 0-20zm6.9 6h-2.9a15 15 0 0 0-1.4-3.6A8 8 0 0 1 18.9 8zM12 4c.8 1.1 1.5 2.5 1.9 4h-3.8c.4-1.5 1.1-2.9 1.9-4zM4.3 14a8 8 0 0 1 0-4h3.4a16 16 0 0 0 0 4zm.8 2h2.9c.3 1.3.8 2.5 1.4 3.6A8 8 0 0 1 5.1 16zM8 8H5.1a8 8 0 0 1 4.3-3.6C8.8 5.5 8.3 6.7 8 8zm4 12c-.8-1.1-1.5-2.5-1.9-4h3.8c-.4 1.5-1.1 2.9-1.9 4zm2.3-6H9.7a14 14 0 0 1 0-4h4.6a14 14 0 0 1 0 4zm.3 5.6c.6-1.1 1.1-2.3 1.4-3.6h2.9a8 8 0 0 1-4.3 3.6zm1.7-5.6a16 16 0 0 0 0-4h3.4a8 8 0 0 1 0 4z"/></svg>
      www.thebrightlearner.example
    </li>
  </ul>

  <ul class="socials">
    <li><span class="marker"></span>@writermilohart</li>
    <li><span class="marker"></span>thebrightlearner</li>
    <li><span class="marker"></span>thebrightlearner</li>
  </ul>
</section>

</body>
</html>
```